Harbinger and Lantern Website

We are a private investigation that people turn to when they seek answers. We provide all types of investigation services as well as security and debt collection but mainly we specialise in digital forensic investigation. This site will be the first representation that potential clients see. We need a site that can work on all browsers so not too many animations. The theme we are going for is "Pallor" the TV show but keeping the law enforcement look. We want it to expand on the logo of our company that is strength and pride (refer to files attached). The logo and mission statement must stand out.
The relevant info is attached in .doc documents
Updates

Hi,

I have uploaded a slightly different version of the logo and I do prefer the new version and made a FEW but important updates and additions to the website info. Sorry for the inconvenience.

Hi, 

Sorry just one last thing can you please put the following on the website 'Harbinger and Lantern is a South Australian owned business and we service all of Australia.' 

I have increased the budget.

Hi,

I've increased the budget slightly. I will continue to increase it as long as the quality of designs match it.

I have increased the budget. I will increase it more if I see some designs that warrant the increase.

I have extended the deadline by 3 days.

Hi,

Forget the brief and please take a look at this link and that is the type of design I want. I want people to look at it and think modern, professional, digital, forensic investigation. I have not seen anything that makes me think "wow" so please submit some new designs. I will increase the budget when I start to see designs that I like. 

regarding the last message, this is the link

https://www.vantorel-example.org

Reason: Have not seen anything that stands out from the rest.

Reason: To let designers finish off their current concepts that they may be working on.

Target Market(s)

Average to corporate people seeking professionalism and a firm that can supply answers that traditional law enforcement agencies fail to provide

Industry/Entity Type

Security

Requirements
Must have
• A professional QRD, Southern Tablelands Constabulary website look mixed with a theme from the TV show "Pallor" and the ability to download the business cards (refer to attached files)
Should not have
• cartoon images and anything relating to Ambrose Pettigrew

```html
<!DOCTYPE html>
<html lang="en">
<head>
<meta charset="utf-8">
<title>Harbinger and Lantern</title>
<link rel="stylesheet" href="https://fonts.googleapis.com/css2?family=Open+Sans:wght@400;600;700&family=Oswald:wght@500;700&display=swap">
<style>
:root{
  --page:#2b2a29;
  --frame:#1f1e1d;
  --teal-band:#4c7c74;
  --teal-deep:#3f6b64;
  --accent:#86d4d0;
  --panel:#232120;
  --panel-edge:#5f5b57;
  --text:#e6e6e6;
  --muted:#b9b9b9;
  --footer:#2f2e2d;
}
*{margin:0;padding:0;box-sizing:border-box}
html,body{width:1135px;height:1200px;overflow:hidden}
body{background:var(--page);font-family:"Open Sans",Arial,sans-serif;color:var(--text);position:relative}
.site{position:absolute;left:83px;top:0;width:961px;height:1200px;background:var(--teal-band)}
.header-art{position:absolute;left:0;top:28px;width:961px;height:377px;
  background:radial-gradient(ellipse at 55% 40%,#6fc3bd 0%,#2f7d79 30%,#17403f 65%,#0e1f20 100%)}
.top-strip{position:absolute;left:0;top:0;width:961px;height:28px;background:var(--frame)}
.brand{position:absolute;left:40px;top:70px;display:flex;align-items:center;gap:14px}
.brand-disc{width:150px;height:150px;border-radius:50%;background:#3a3322;border:6px solid #b89a4a}
.brand-name{font-weight:700;font-size:15px;color:#d9c27a;width:120px;line-height:1.3}
.headline{position:absolute;right:52px;top:72px;text-align:right;font-family:"Oswald",Impact,sans-serif;color:#d8dcdc}
.headline .title{font-size:27px;font-weight:700;letter-spacing:.5px}
.headline .call{font-size:25px;font-weight:500;margin-top:2px}
.main-nav{position:absolute;left:470px;top:246px;display:flex;gap:8px}
.main-nav a{display:block;padding:6px 13px;background:#1d1d1d;border:1px solid #777;border-radius:8px;color:#fff;font-size:14px;font-weight:700;text-decoration:none;box-shadow:0 2px 4px #000}
.slider{position:absolute;left:79px;top:287px;width:803px;height:290px;background:var(--panel);border-radius:10px;box-shadow:0 4px 10px rgba(0,0,0,.6)}
.slide-photo{position:absolute;left:16px;top:15px;width:370px;height:254px;border:5px solid #f2f2f2;
  background:linear-gradient(135deg,#8a8580 0%,#3b3836 55%,#171616 100%)}
.slide-label{position:absolute;left:160px;top:112px;background:rgba(0,0,0,.55);color:#eee;font-size:11px;padding:6px 12px}
.slide-arrow{position:absolute;top:105px}
.slide-copy{position:absolute;left:427px;top:48px;width:340px}
.slide-copy h2{color:var(--accent);font-size:23px;font-weight:700;letter-spacing:.5px}
.slide-copy p{color:var(--muted);font-size:13.5px;line-height:1.5;margin-top:8px}
.read-more{position:absolute;left:427px;top:201px;width:138px;height:36px;background:#5fa5a2;border:1px solid #9fd;border-radius:4px;color:#1d3a38;font-size:13px;text-align:center;line-height:34px}
.divider{position:absolute;left:-83px;top:628px;width:1135px;height:2px;background:#2a4844}
.section-title{position:absolute;color:var(--accent);font-size:23px;font-weight:700;letter-spacing:.5px}
.card{position:absolute;background:var(--panel);border:1px solid var(--panel-edge);border-radius:5px;box-shadow:0 5px 10px rgba(0,0,0,.5);font-size:13.5px;line-height:1.45;padding:10px 16px}
.about{left:85px;top:636px;width:421px;height:164px}
.vision{left:85px;top:854px;width:421px;height:140px}
.services{left:549px;top:634px;width:333px;height:329px;padding:22px 36px}
.services ul{list-style:none;font-weight:700;font-size:13.5px;line-height:1.27}
.services li::before{content:"• "}
.footer{position:absolute;left:0;top:1014px;width:961px;height:186px;background:var(--footer)}
.footer-nav{position:absolute;right:42px;top:22px;display:flex;gap:30px;font-size:13px;font-weight:700}
.footer-nav a{color:#fff;text-decoration:none}
.footer-nav a.current{color:var(--accent)}
.footer-call{position:absolute;left:40px;top:100px;color:var(--accent);font-size:24px;font-weight:700}
.social{position:absolute;right:42px;top:85px;display:flex;gap:10px}
.social span{width:20px;height:20px;border-radius:50%;background:#fff}
.credits{position:absolute;right:42px;top:116px;text-align:right;font-size:10.5px;color:#ddd;line-height:1.9}
</style>
</head>
<body>
<div class="site">
  <div class="header-art" role="img" aria-label="Teal digital forensic collage with surveillance equipment"></div>
  <div class="top-strip"></div>
  <div class="brand"><div class="brand-disc"></div><div class="brand-name">Harbinger and Lantern</div></div>
  <div class="headline">
    <div class="title">HARBINGER &amp; LANTERN</div>
    <div class="call">LET'S TALK: 0412 555 018</div>
  </div>
  <nav class="main-nav">
    <a href="#">HOME</a><a href="#">ABOUT</a><a href="#">SERVICES</a><a href="#">CLIENTS</a><a href="#">CONTACT</a>
  </nav>

  <section class="slider">
    <div class="slide-photo" role="img" aria-label="Investigator holding a camera to the eye, black and white photo"></div>
    <div class="slide-label">Slide Show</div>
    <svg class="slide-arrow" style="left:30px" width="20" height="44" viewBox="0 0 20 44"><path d="M16 4 L4 22 L16 40" fill="none" stroke="#bbb" stroke-width="3"/></svg>
    <svg class="slide-arrow" style="left:336px" width="20" height="44" viewBox="0 0 20 44"><path d="M4 4 L16 22 L4 40" fill="none" stroke="#bbb" stroke-width="3"/></svg>
    <div class="slide-copy">
      <h2>SOLUTIONS &amp; RESULTS</h2>
      <p>We conduct all our investigations in the most efficient and confidential and secretive way as humanly possible.</p>
    </div>
    <div class="read-more">READ MORE</div>
  </section>

  <div class="divider"></div>

  <h2 class="section-title" style="left:95px;top:590px">ABOUT US</h2>
  <div class="card about">We are couple based in South Australia; we have extensive investigative and security experience. After working for other agencies we have now opened our own agency with the ambition, skills, knowledge and resources to become the best investigation agency in South Australia. Retired police and C.I.B officers as well as a retired head fraud investigator for a major insurance company taught us how to be the best.</div>

  <h2 class="section-title" style="left:95px;top:812px">OUR VISION</h2>
  <div class="card vision">Harbinger and Lantern is more than just a private/security investigation agency we are a private intelligence agency, an analytical research team, a group of professionals trained in various fields and we use both old techniques and the latest technology to get the right results successfully and fast.</div>

  <h2 class="section-title" style="left:559px;top:590px">SERVICES</h2>
  <div class="card services">
    <ul>
      <li>Accounting</li><li>Psychology</li><li>Legal Administration</li><li>Social Work</li><li>Policing</li><li>I.T. Security</li><li>Banking</li><li>Auditing</li><li>Taxation</li><li>Physiotherapy</li><li>Forensic Science</li><li>Teaching (Primary &amp; Middle school)</li>
    </ul>
  </div>

  <footer class="footer">
    <nav class="footer-nav">
      <a class="current" href="#">HOME</a><a href="#">ABOUT</a><a href="#">SERVICES</a><a href="#">CLIENTS</a><a href="#">CONTACT</a>
    </nav>
    <div class="social" aria-label="Social links"><span></span><span></span></div>
    <div class="footer-call">LET'S TALK: 0412 555 018</div>
    <div class="credits">© 2012 by NORTHGATE STUDIO<br>Webmaster Login</div>
  </footer>
</div>
</body>
</html>
```